Wildlfower Field Guide Needs a Book Cover Design

We need a book cover design in formats compatible with Adobe Illustrator and/or Photoshop (vector file that can be edited). I have attached a Power Point file with the general design features for the front and back covers and photographs to be used in the book cover. The cover size is 6" wide by 9" high (same size as the attached Power Point file). The book cover should have the same format including photos as the attached file with a similar color scheme. We are looking for a sky blue background then title text in a complementary darker blue. The other color elements (borders around photos) can be the same darker blue or dark gray. We are looking for better text types/styles for the title than those is the attached file. All three lines of the title should have the same width (1st line - thicker text, 2nd line - white italics on dark background, 3rd line - narrow text). The dark background on the 2nd line would ideally have some texture or style like a trail. On the back cover, written paragraphs should remain in Ebrima font.

Requirements
Must have
• Project should follow general cover outline of attached Power Point file
• Should have desired color scheme
• Must include all photos as formatted in the attached in the Power point file
Nice to have
• The title (2nd line) can be a solid color matching 1st line text or texture like a hiking trail

```html
<!DOCTYPE html>
<html lang="en">
<head>
<meta charset="utf-8">
<title>Desert Blooms Beside the Path – Cover</title>
<link rel="stylesheet" href="https://fonts.googleapis.com/css2?family=Barlow:ital,wght@0,800;1,500&family=Barlow+Condensed:wght@600&family=Noto+Sans:wght@400&display=swap">
<style>
  :root {
    --page-bg: #ffffff;
    --cover-sky: #cde0ef;
    --title-blue: #1b6fb8;
    --band-blue: #1e6db6;
    --frame-navy: #163f66;
    --grid-line: #1c1c1c;
    --white: #ffffff;
  }
  html, body {
    margin: 0;
    padding: 0;
    width: 1200px;
    height: 1106px;
    overflow: hidden;
    background: var(--page-bg);
  }
  .cover {
    position: absolute;
    left: 231px;
    top: 0;
    width: 737px;
    height: 1106px;
    background: var(--cover-sky);
  }
  .title-block {
    position: absolute;
    left: 0;
    top: 0;
    width: 737px;
    height: 340px;
  }
  .title-main {
    font-family: "Barlow", sans-serif;
    font-weight: 800;
    font-size: 92px;
    fill: var(--title-blue);
  }
  .title-path {
    font-family: "Barlow", sans-serif;
    font-style: italic;
    font-weight: 500;
    font-size: 56px;
    fill: var(--white);
  }
  .title-region {
    font-family: "Barlow Condensed", sans-serif;
    font-weight: 600;
    font-size: 58px;
    fill: var(--title-blue);
  }
  .photo-grid {
    position: absolute;
    left: 76px;
    top: 349px;
    width: 586px;
    height: 607px;
    box-sizing: border-box;
    border: 3px solid var(--frame-navy);
    display: grid;
    grid-template-columns: repeat(3, 1fr);
    grid-template-rows: repeat(3, 1fr);
    gap: 1px;
    background: var(--grid-line);
  }
  .photo-tile {
    background: radial-gradient(circle at 50% 50%, #f2d83a 0%, #e5c92c 30%, #6f6d4c 55%, #4c4f43 100%);
  }
  .photo-tile.daisy {
    background: radial-gradient(circle at 50% 50%, #e8a83a 0%, #f4d52c 18%, #edcf2a 40%, #7a7a62 62%, #5a5e55 100%);
  }
  .author {
    position: absolute;
    left: 0;
    top: 966px;
    margin: 0;
    width: 737px;
    text-align: center;
    font-family: "Noto Sans", sans-serif;
    font-weight: 400;
    font-size: 50px;
    line-height: 1;
    color: var(--title-blue);
  }
</style>
</head>
<body>
  <main class="cover">
    <svg class="title-block" viewBox="0 0 737 340" width="737" height="340">
      <text class="title-main" x="76" y="164" textLength="581" lengthAdjust="spacingAndGlyphs">DESERT BLOOMS</text>
      <rect class="title-band" x="74" y="180" width="583" height="80" fill="var(--band-blue)"/>
      <text class="title-path" x="110" y="239" textLength="515" lengthAdjust="spacingAndGlyphs">Beside the Path</text>
      <text class="title-region" x="76" y="316" textLength="581" lengthAdjust="spacingAndGlyphs">Saguaro Country Hikes</text>
    </svg>

    <section class="photo-grid">
      <div class="photo-tile" role="img" aria-label="Yellow four-petalled desert flower with red centre"></div>
      <div class="photo-tile" role="img" aria-label="Yellow four-petalled evening primrose"></div>
      <div class="photo-tile" role="img" aria-label="Pale yellow five-petalled flower"></div>
      <div class="photo-tile" role="img" aria-label="Yellow flower with crinkled petals among grey leaves"></div>
      <div class="photo-tile" role="img" aria-label="Small yellow five-petalled flower"></div>
      <div class="photo-tile" role="img" aria-label="Yellow flower with narrow notched petals"></div>
      <div class="photo-tile daisy" role="img" aria-label="Yellow daisy-like flower"></div>
      <div class="photo-tile daisy" role="img" aria-label="Yellow daisy with orange centre"></div>
      <div class="photo-tile daisy" role="img" aria-label="Yellow many-rayed desert daisy"></div>
    </section>

    <p class="author">Daniel Hartwell</p>
  </main>
</body>
</html>
```